Business card design

I need my logo on this card, things I need the card to have on it
licensed and insured.
owner operators Derek & Milton Halvorsen
my phone number 5418237906
Disaster Recovery, Storm Damage Restoration, Proactive Disaster Plan Management, Roof Repair/Restoration Structural Repair and Reconstruction, Emergency Boarding and Tarping Service, Perimeter Fencing, Emergency Tree Removal,

```html
<!DOCTYPE html>
<html lang="en">
<head>
<meta charset="utf-8">
<title>Halvorsen's Construction – Business Card</title>
<link href="https://fonts.googleapis.com/css2?family=Exo+2:wght@400;500&family=Montserrat:wght@400;500;600&family=Questrial&family=Quicksand:wght@600&display=swap" rel="stylesheet">
<style>
  :root {
    --bg: #d4d5d8;
    --blue: #3c92d0;
    --white: #ffffff;
    --ink: #4a4a4c;
    --grey: #6d6e71;
  }
  * { margin: 0; padding: 0; box-sizing: border-box; }
  html, body { width: 900px; height: 1200px; overflow: hidden; }
  body { background: var(--bg); position: relative; font-family: "Questrial", sans-serif; }

  .card { position: absolute; left: 133px; width: 633px; height: 364px; }
  .card--front { top: 210px; background: var(--blue); color: var(--white); }
  .card--back { top: 624px; background: var(--white); color: var(--ink); }

  .brand { position: absolute; text-align: center; font-family: "Montserrat", sans-serif; font-weight: 400; }
  .brand__mark { display: block; width: 40px; height: 40px; margin: 0 auto 16px; }
  .brand__name { display: block; font-size: 30px; letter-spacing: 0.5px; line-height: 1; }
  .brand__sub { display: block; font-size: 10px; letter-spacing: 7.2px; margin-top: 8px; }
  .card--front .brand { left: 40px; top: 112px; width: 260px; color: var(--white); }
  .card--front .brand__mark { background: var(--white); }
  .card--back .brand { left: 30px; top: 112px; width: 260px; color: var(--blue); }
  .card--back .brand__mark { background: var(--blue); }

  .services { position: absolute; left: 329px; top: 44px; font-family: "Exo 2", sans-serif; }
  .services__title { font-family: "Montserrat", sans-serif; font-weight: 500; font-size: 16.5px; letter-spacing: 0.3px; margin-bottom: 10px; }
  .services__list { list-style: none; font-size: 13.5px; line-height: 22.5px; letter-spacing: 0.3px; }
  .services__item { position: relative; padding-left: 20px; margin-bottom: 7.5px; }
  .services__icon { position: absolute; left: 0; top: 4px; width: 13px; height: 12px; }

  .divider { position: absolute; left: 308px; top: 95px; width: 1px; height: 176px; background: var(--grey); }
  .contact { position: absolute; left: 327px; top: 92px; font-size: 15px; letter-spacing: 0.4px; }
  .contact__name { font-family: "Quicksand", sans-serif; font-weight: 600; font-size: 21px; color: var(--blue); letter-spacing: 0.2px; line-height: 24px; }
  .contact__role { margin-top: 2px; line-height: 20px; }
  .contact__address { margin-top: 9px; line-height: 25px; }
  .contact__lines { margin-top: 7px; list-style: none; }
  .contact__line { position: relative; padding-left: 22px; line-height: 23px; }
  .contact__line--phone { font-size: 16px; letter-spacing: 1px; }
  .contact__icon { position: absolute; left: 0; top: 5px; width: 14px; height: 14px; }

  .credential { position: absolute; left: 0; right: 0; top: 307px; display: flex; align-items: center; gap: 8px; }
  .credential__rule { flex: 1; height: 1px; background: var(--blue); }
  .credential__text { font-family: "Montserrat", sans-serif; font-weight: 600; font-size: 15px; color: var(--grey); letter-spacing: 0.3px; }
</style>
</head>
<body>
  <svg width="0" height="0" style="position:absolute">
    <defs>
      <symbol id="icon-house" viewBox="0 0 13 12">
        <path d="M6.5 0 L13 5 L11.5 5 L11.5 12 L1.5 12 L1.5 5 L0 5 Z" fill="currentColor"/>
        <rect x="3.2" y="6" width="2.3" height="3" fill="#3c92d0"/>
        <rect x="7.5" y="6" width="2.3" height="3" fill="#3c92d0"/>
      </symbol>
    </defs>
  </svg>

  <section class="card card--front">
    <div class="brand">
      <span class="brand__mark"></span>
      <span class="brand__name">HALVORSEN'S</span>
      <span class="brand__sub">CONSTRUCTION L.L.C</span>
    </div>
    <div class="services">
      <h2 class="services__title">OUR SERVICES:</h2>
      <ul class="services__list">
        <li class="services__item"><svg class="services__icon"><use href="#icon-house"/></svg>Disaster Recovery</li>
        <li class="services__item"><svg class="services__icon"><use href="#icon-house"/></svg>Storm Damage Restoration</li>
        <li class="services__item"><svg class="services__icon"><use href="#icon-house"/></svg>Proactive Disaster Plan Management</li>
        <li class="services__item"><svg class="services__icon"><use href="#icon-house"/></svg>Roof Repair/Restoration Structural<br>Repair and Reconstruction</li>
        <li class="services__item"><svg class="services__icon"><use href="#icon-house"/></svg>Emergency Boarding and<br>Tarping Service</li>
        <li class="services__item"><svg class="services__icon"><use href="#icon-house"/></svg>Perimeter Fencing</li>
        <li class="services__item"><svg class="services__icon"><use href="#icon-house"/></svg>Emergency Tree Removal</li>
      </ul>
    </div>
  </section>

  <section class="card card--back">
    <div class="brand">
      <span class="brand__mark"></span>
      <span class="brand__name">HALVORSEN'S</span>
      <span class="brand__sub">CONSTRUCTION L.L.C</span>
    </div>
    <div class="divider"></div>
    <div class="contact">
      <h1 class="contact__name">Derek &amp; Milton Halvorsen</h1>
      <p class="contact__role">Owner Operator</p>
      <p class="contact__address">447 Willow Bend Rd,<br>Greenville, SC 29607</p>
      <ul class="contact__lines">
        <li class="contact__line contact__line--phone">
          <svg class="contact__icon" viewBox="0 0 14 14"><path d="M3 0.8 L5 3.6 L3.9 5.2 C4.6 7 6.8 9.3 8.8 10.1 L10.4 9 L13.2 11 L12 13.2 C6.5 13.5 0.5 7.5 0.8 2 Z" fill="#3c92d0"/></svg>5418237906</li>
        <li class="contact__line">
          <svg class="contact__icon" viewBox="0 0 14 14"><rect x="0.5" y="3" width="13" height="9" fill="#3c92d0"/><path d="M0.5 3 L7 8.2 L13.5 3" fill="none" stroke="#fff" stroke-width="1.2"/></svg>info@halvorsenconstructionllc.com</li>
        <li class="contact__line">
          <svg class="contact__icon" viewBox="0 0 14 14" fill="none" stroke="#3c92d0" stroke-width="1.1"><circle cx="7" cy="7" r="6"/><ellipse cx="7" cy="7" rx="2.6" ry="6"/><path d="M1 7 H13 M2 4 H12 M2 10 H12"/></svg>halvorsenconstructionllc.com</li>
      </ul>
    </div>
    <div class="credential">
      <span class="credential__rule"></span>
      <span class="credential__text">LICENSED AND INSURED</span>
      <span class="credential__rule"></span>
    </div>
  </section>
</body>
</html>
```